2021 Summer Ads Whitmore Ash Custom Homes

We need a re-design of our summer ad run for our customer, Whitmore Ash Custom Homes. They are custom home builders in the mostly rural parts of West Virginia, USA. They are known for their "Forever Home" tagline. We'd like two designed ads with the main difference being just the custom home that's featured. These designs should be for a Google banner like 300 x 250 and square ad like 250 x 250. For inspiration please visit the Whitmore Ash Custom Homes website at www dot whitmoreashcustomhomes dot com

Target Market(s)

consumers / new home shoppers

Industry/Entity Type

Consumer

Requirements
Must have
• WACH logo
Price Lock Available!
Custom home pic
Learn more >
small QVTG logo mark

```html
<!DOCTYPE html>
<html lang="en">
<head>
<meta charset="utf-8">
<title>Whitmore Ash Custom Homes – Summer Ad</title>
<link href="https://fonts.googleapis.com/css2?family=Passion+One:wght@400;700&family=Montserrat:wght@600;700&display=swap" rel="stylesheet">
<style>
  :root {
    --night: #1c2229;
    --night-deep: #12161b;
    --slate: #3a4049;
    --brand-red: #e2222e;
    --brand-red-dark: #a8121c;
    --white: #ffffff;
    --sky: #6fa6d8;
    --siding: #e9ecef;
    --foliage: #3e6b34;
  }
  html, body {
    margin: 0;
    padding: 0;
    overflow: hidden;
    background: var(--night-deep);
  }
  .ad {
    position: relative;
    width: 1200px;
    height: 1000px;
    overflow: hidden;
    background: var(--night);
    font-family: "Montserrat", Arial, sans-serif;
    color: var(--white);
  }
  .ad__art {
    position: absolute;
    inset: 0;
  }
  .brand {
    position: absolute;
    left: 56px;
    top: 110px;
    width: 380px;
    font-family: "Passion One", Impact, sans-serif;
    font-weight: 400;
    font-size: 62px;
    line-height: 0.95;
    letter-spacing: 1px;
    text-transform: uppercase;
    color: var(--white);
  }
  .headline {
    position: absolute;
    left: 56px;
    top: 356px;
    margin: 0;
    font-family: "Passion One", Impact, sans-serif;
    font-weight: 400;
    font-size: 86px;
    line-height: 88px;
    letter-spacing: 2px;
    text-transform: uppercase;
  }
  .offer {
    position: absolute;
    left: 56px;
    top: 718px;
    margin: 0;
    font-weight: 700;
    font-size: 30px;
    letter-spacing: 1px;
    text-transform: uppercase;
  }
  .cta {
    position: absolute;
    left: 56px;
    top: 826px;
    width: 314px;
    height: 86px;
    box-sizing: border-box;
    border: 3px solid var(--white);
    border-radius: 8px;
    display: flex;
    align-items: center;
    justify-content: center;
    gap: 22px;
    font-weight: 600;
    font-size: 25px;
    letter-spacing: 1px;
    text-transform: uppercase;
    color: var(--white);
    text-decoration: none;
  }
  .cta__icon {
    width: 44px;
    height: 44px;
  }
  .member-mark {
    position: absolute;
    left: 436px;
    top: 820px;
    display: flex;
    align-items: center;
    gap: 14px;
    font-family: "Passion One", Impact, sans-serif;
    font-size: 74px;
    line-height: 1;
    color: var(--white);
  }
  .member-mark__square {
    width: 26px;
    height: 26px;
    background: var(--white);
  }
</style>
</head>
<body>
<div class="ad">
  <svg class="ad__art" width="1200" height="1000" viewBox="0 0 1200 1000">
    <defs>
      <linearGradient id="night-scene" x1="0" y1="0" x2="1" y2="1">
        <stop offset="0" stop-color="#2b333d"/>
        <stop offset="0.5" stop-color="#1d232b"/>
        <stop offset="1" stop-color="#0f1317"/>
      </linearGradient>
      <linearGradient id="home-scene" x1="0" y1="0" x2="0" y2="1">
        <stop offset="0" stop-color="#7fb1de"/>
        <stop offset="0.28" stop-color="#3a3d42"/>
        <stop offset="0.6" stop-color="#e6e9ec"/>
        <stop offset="0.85" stop-color="#2a2d33"/>
        <stop offset="1" stop-color="#6b6e72"/>
      </linearGradient>
      <linearGradient id="red-band" x1="0" y1="0" x2="1" y2="0">
        <stop offset="0" stop-color="#b5141f"/>
        <stop offset="1" stop-color="#ec2430"/>
      </linearGradient>
    </defs>

    <rect class="backdrop" width="1200" height="1000" fill="url(#night-scene)"
          role="img" aria-label="Dimmed evening photo of a custom-built house behind the headline"/>

    <polygon class="chevron chevron--shadow" fill="#4a5059" opacity="0.45"
             points="700,0 810,0 540,470 840,1000 740,1000 450,470"/>
    <polygon class="chevron chevron--red" fill="url(#red-band)"
             points="810,0 885,0 610,470 925,1000 840,1000 540,470"/>
    <polygon class="chevron chevron--deep" fill="#2a2f36"
             points="885,0 910,0 640,470 950,1000 925,1000 610,470"/>

    <polygon class="feature-home" fill="url(#home-scene)"
             points="910,0 1200,0 1200,1000 950,1000 640,470"
             role="img" aria-label="Photo of a white board-and-batten custom home with a steep gable roof and three black carriage garage doors"/>
  </svg>

  <div class="brand">Whitmore Ash<br>Custom Homes</div>

  <h1 class="headline">Start<br>Building<br>Your Forever<br>Home Today</h1>

  <p class="offer">Price Lock Available!</p>

  <a class="cta" href="#">
    Learn More
    <svg class="cta__icon" viewBox="0 0 44 44" aria-hidden="true">
      <circle cx="22" cy="22" r="22" fill="var(--brand-red)"/>
      <polyline points="18,13 27,22 18,31" fill="none" stroke="#fff" stroke-width="4" stroke-linecap="round" stroke-linejoin="round"/>
    </svg>
  </a>

  <div class="member-mark">
    <span class="member-mark__square"></span>QVTG
  </div>
</div>
</body>
</html>
```